Harbor Bean Packaging layout is already done in brief.

A bag we can then add stickers to with all the different blends, bag that will embody the follow. Please don’t copy existing designs.

Harbor Bean was born 2011, From that moment we took a dive deep into complex journey that coffee takes us on.

Harbor felt like a name that was easy to say, easy to recognise, and a feeling everyone is seeking. Its taking a moment, a moment to HARBOR, illuminate and elevate.

We fully embrace the art and science throughout the entire coffee chain — including sourcing all kinds of coffees which feature different processing methods, roast profiles, and brew methods. And we want our customers to see that hard work and experimentation.

When sourcing coffees we put the planet , people and quality before profit.. We also look at variety, country, process, and pricing but not until these element meet our standards.

We strive to product our products with the most sustainable means, deliver them with most efficient transport possible and wrap them with love using only compostable or reusable packaging.

Our transparency model was born out of our interactions: being told that certain green coffee information wasn’t available, that you can’t buy a coffee a certain way, that you can’t pay high prices for coffee and make it, that you can’t be transparent.

We want to continue to push the industry and ourselves forward by increasing our sourcing standards and innovating throughout the process of buying green, roasting, brewing, and serving customers. We hope our customers continue to enjoy beautiful cups of black coffee over breakfast, meetings, dates, and any occasion that calls for something intentional.

Target Market(s)

Boomers, Hipsters

Industry/Entity Type

Coffee

Font styles to use
Other font styles liked:
• Cooper

Requirements
Must have
• Seeking Simpler Times..
Nice to have
• Check: Lurid Coffee, Meadowfold Roasters, Pelican Cofeee, Fox&Reed cool bags we like. Maybe some Foil or, Embossing
Should not have
• Try o busy

```html
<!DOCTYPE html>
<html lang="en">
<head>
<meta charset="utf-8">
<title>Harbor Bean – Organic Speciality Coffee Bag</title>
<link rel="stylesheet" href="https://fonts.googleapis.com/css2?family=Montserrat:wght@400;700&display=swap">
<style>
  :root {
    --bag-black: #000000;
    --ink-white: #ffffff;
    --art-light: #e9e9e9;
    --art-mid: #bdbdbd;
  }
  * { margin: 0; padding: 0; box-sizing: border-box; }
  html, body {
    width: 864px;
    height: 1200px;
    overflow: hidden;
    background: var(--bag-black);
  }
  .bag {
    position: relative;
    width: 864px;
    height: 1200px;
    background: var(--bag-black);
    color: var(--ink-white);
    font-family: "Montserrat", Arial, sans-serif;
  }
  .bag__title {
    position: absolute;
    top: 60px;
    left: 0;
    width: 864px;
    text-align: center;
    font-weight: 700;
    font-size: 21px;
    letter-spacing: 0.6px;
  }
  .rule {
    position: absolute;
    left: 48px;
    height: 2px;
    display: block;
  }
  .rule line {
    stroke: var(--ink-white);
    stroke-width: 1.4;
    stroke-dasharray: 11 15.5;
  }
  .rule--top    { top: 126px; }
  .rule--mid-1  { top: 485px; }
  .rule--mid-2  { top: 713px; }
  .rule--foot   { top: 1107px; }

  .value__art {
    position: absolute;
    background: linear-gradient(160deg, var(--art-light), var(--art-mid));
    border-radius: 6px;
  }
  .value__art--pour        { left: 49px; top: 288px; width: 168px; height: 167px; }
  .value__art--globe       { left: 49px; top: 524px; width: 168px; height: 156px; }
  .value__art--portafilter { left: 95px; top: 746px; width: 74px;  height: 167px; }

  .value__text {
    position: absolute;
    left: 288px;
    width: 540px;
    font-size: 18.6px;
    line-height: 24.4px;
    font-weight: 400;
    letter-spacing: 0.25px;
    white-space: nowrap;
  }
  .value__text--story   { top: 323px; }
  .value__text--planet  { top: 527px; }
  .value__text--craft   { top: 767px; }

  .bag__weight {
    position: absolute;
    left: 48px;
    top: 1126px;
    font-size: 19px;
    letter-spacing: 0.3px;
  }
  .brand {
    position: absolute;
    left: 535px;
    top: 1100px;
    display: flex;
    align-items: center;
  }
  .brand__mark {
    width: 47px;
    height: 47px;
    border: 5px solid var(--ink-white);
    border-radius: 50%;
    margin-right: 16px;
  }
  .brand__copy { display: flex; flex-direction: column; }
  .brand__name {
    font-weight: 700;
    font-size: 27px;
    line-height: 28px;
    letter-spacing: 0.2px;
  }
  .brand__url {
    font-size: 18.6px;
    line-height: 24px;
    letter-spacing: 0.3px;
  }
</style>
</head>
<body>
<main class="bag">
  <h1 class="bag__title">ORGANIC SPECIALITY COFFEE</h1>

  <svg class="rule rule--top" width="770" height="2" aria-hidden="true"><line x1="0" y1="1" x2="770" y2="1"/></svg>

  <section class="value">
    <div class="value__art value__art--pour" role="img" aria-label="Line illustration of a barista in an apron pouring from a gooseneck kettle into a pour-over brewer"></div>
    <p class="value__text value__text--story">Born in 2011, Harbor Bean took a deep dive into<br>the complex journey coffee takes us on. A moment<br>to harbor, illuminate and elevate.<br>Seeking Simpler Times..</p>
  </section>

  <svg class="rule rule--mid-1" width="770" height="2" aria-hidden="true"><line x1="0" y1="1" x2="770" y2="1"/></svg>

  <section class="value">
    <div class="value__art value__art--globe" role="img" aria-label="Line illustration of two open hands holding up the globe"></div>
    <p class="value__text value__text--planet">We put the planet, people and quality before profit.<br>We produce with the most sustainable means, choose<br>the most efficient transport possible and wrap every<br>bag with love in compostable or reusable packaging.<br>Follow as we push our sourcing standards higher<br>every year.</p>
  </section>

  <svg class="rule rule--mid-2" width="770" height="2" aria-hidden="true"><line x1="0" y1="1" x2="770" y2="1"/></svg>

  <section class="value">
    <div class="value__art value__art--portafilter" role="img" aria-label="Line illustration of a hand holding an espresso portafilter with a city skyline inside the basket"></div>
    <p class="value__text value__text--craft">We embrace the art and science of the whole coffee<br>chain, from sourcing and processing to roasting<br>and brewing. We share our green coffee details<br>openly, and hope you enjoy beautiful black cups<br>for breakfast, meetings, dates and beyond.</p>
  </section>

  <svg class="rule rule--foot" width="433" height="2" aria-hidden="true"><line x1="0" y1="1" x2="433" y2="1"/></svg>

  <p class="bag__weight">300 gram</p>

  <div class="brand">
    <span class="brand__mark" aria-hidden="true"></span>
    <div class="brand__copy">
      <span class="brand__name">Harbor Bean</span>
      <span class="brand__url">www.harborbean.nz</span>
    </div>
  </div>
</main>
</body>
</html>
```